Business Card for my New Brokerage

Looking to get a business card design for my new Real Estate Brokerage.
I want it with Picture, Phone Number, Email, Website, Office Address
Name and Designation. Please add logo too.

Target Market(s)

Real Estate Investors or Home Buyers

Industry/Entity Type

Real Estate

Contact Information for Business Card

Name, Email, Phone Number, website, email, office address

Colors
EB3D1F
EC4F4E
F09395
F8D3D4
FCEDEE

Requirements
Must have
• Minimalistic, Clean, Modern, Photo
Nice to have
• White and Red Colors

```html
<!DOCTYPE html>
<html lang="en">
<head>
<meta charset="utf-8">
<title>Ember Realty Inc – Business Card</title>
<link href="https://fonts.googleapis.com/css2?family=Montserrat:wght@400;600;700;800&display=swap" rel="stylesheet">
<style>
  :root {
    --brand-red: #dd0a17;
    --card-white: #ffffff;
    --card-edge: #d9d9d9;
    --page-bg: #ffffff;
    --photo-dark: #1d2a44;
    --photo-light: #eef0f4;
  }
  * { margin: 0; padding: 0; box-sizing: border-box; }
  html, body {
    width: 1200px; height: 1200px; overflow: hidden;
    background: var(--page-bg);
    font-family: "Montserrat", sans-serif;
    color: var(--brand-red);
  }
  .sheet { position: relative; width: 1200px; height: 1200px; }
  .card {
    position: absolute; left: 336px; width: 571px; height: 385px;
    background: var(--card-white);
    border: 1px solid var(--card-edge);
  }
  .card--front { top: 179px; }
  .card--back { top: 591px; }

  .brand { position: absolute; text-align: center; font-weight: 700; color: var(--brand-red); }
  .brand__name { display: block; line-height: 1; }
  .brand__sub { display: block; line-height: 1; }

  .card--front .brand { left: 0; right: 0; top: 150px; }
  .card--front .brand__name { font-size: 82px; letter-spacing: 1px; }
  .card--front .brand__sub { font-size: 24px; letter-spacing: 9px; margin-top: 10px; padding-left: 9px; }

  .portrait {
    position: absolute; left: 35px; top: 14px; width: 190px; height: 355px;
    background: linear-gradient(180deg, var(--photo-light) 0%, #c9ced8 30%, var(--photo-dark) 60%, var(--photo-dark) 100%);
  }

  .details { position: absolute; left: 344px; top: 40px; }
  .details .brand { position: static; text-align: left; width: 135px; }
  .details .brand__name { font-size: 37px; text-align: center; }
  .details .brand__sub { font-size: 10.5px; letter-spacing: 3px; margin-top: 4px; text-align: center; }

  .contact { margin-top: 40px; font-size: 15.5px; line-height: 19px; font-weight: 400; }
  .contact__name { font-weight: 800; font-size: 15px; }
  .contact__strong { font-weight: 700; }
  .divider { width: 47px; height: 1px; background: var(--brand-red); margin: 22px 0 20px; }
</style>
</head>
<body>
<main class="sheet">
  <section class="card card--front">
    <div class="brand">
      <span class="brand__name">EMBER</span>
      <span class="brand__sub">REALTY INC</span>
    </div>
  </section>

  <section class="card card--back">
    <div class="portrait" role="img" aria-label="Portrait photo of the agent in a dark suit"></div>
    <div class="details">
      <div class="brand">
        <span class="brand__name">EMBER</span>
        <span class="brand__sub">REALTY INC</span>
      </div>
      <div class="contact">
        <p class="contact__name">DANIEL REYES</p>
        <p>dan@ember.com</p>
        <p>123 456 789</p>
        <div class="divider"></div>
        <p class="contact__strong">www.ember.com</p>
        <p>info@ember.com</p>
        <div class="divider"></div>
        <p>Street xxxx, 123</p>
        <p>456 xxx xxxxxx</p>
      </div>
    </div>
  </section>
</main>
</body>
</html>
```